Mineral Drinking Water Label Design

We need a label design for a new bottled drinking water based in (either Pwani or Dar Es Salaam, decision is not yet finalized), Tanzania on the coast of East Africa.

We will use underground aquifers as our only source of raw water(pre treated water).

Which will then be treated through osmosis process, then the mineral water will be bottled in standard 500ml, 1000ml and 1500 ml plastic PET bottles for customer consumption.

We have a vision of expanding our supply network to cover the entire country. Therefore, we expect the label to communicate trust, purity, cleanliness, healthiness of water contained.

The uniqueness and attractiveness of the label/logo is of utmost importance.

With regards to water brand name, we prefer that you use your own imagination and creativity to come up with a name that might be more suited to your individual design.

Note: Different shades of blue are mainly associated with drinking water in Tanzania, however feel free to use any other colors.

Target Market(s)

Upper Class citizens, Hotels, Large Supermarkets etc

Font styles to use
Script

Colors

Designer to choose colors to be used in the design.

```html
<!DOCTYPE html>
<html lang="en">
<head>
<meta charset="utf-8">
<title>Safira Purity Water – 500ml Label</title>
<link rel="stylesheet" href="https://fonts.googleapis.com/css2?family=Marcellus&family=Noto+Serif:wght@400&display=swap">
<style>
  :root {
    --backdrop: #eeeff0;
    --label-film: #f7f8f9;
    --label-edge: #dde0e3;
    --ocean-blue: #1168b6;
    --splash-light: #2a82c8;
    --splash-deep: #1168b6;
    --foam-white: #ffffff;
  }
  html, body {
    margin: 0;
    padding: 0;
    width: 1200px;
    height: 1200px;
    overflow: hidden;
    background: var(--backdrop);
  }
  .canvas {
    position: relative;
    width: 1200px;
    height: 1200px;
    background: radial-gradient(circle at 50% 45%, #fafafa 0%, var(--backdrop) 75%);
  }
  .label-band {
    position: absolute;
    left: 80px;
    top: 120px;
    width: 1040px;
    height: 960px;
    background: var(--label-film);
    border: 2px solid var(--label-edge);
    box-sizing: border-box;
  }
  .badge {
    position: absolute;
    left: 150px;
    top: 150px;
    width: 900px;
    height: 900px;
  }
  .badge svg { position: absolute; inset: 0; }
  .brand-mark {
    position: absolute;
    left: 0;
    right: 0;
    top: 110px;
    display: flex;
    flex-direction: column;
    align-items: center;
    color: var(--foam-white);
  }
  .brand-dot {
    width: 130px;
    height: 130px;
    border-radius: 50%;
    background: var(--foam-white);
    margin-bottom: 50px;
  }
  .brand-name {
    font-family: "Marcellus", serif;
    font-size: 210px;
    line-height: 1;
    letter-spacing: 4px;
  }
  .tagline {
    align-self: flex-end;
    margin-right: 70px;
    margin-top: 6px;
    font-family: "Noto Serif", serif;
    font-size: 58px;
    letter-spacing: 2px;
  }
  .volume {
    position: absolute;
    right: 180px;
    bottom: 130px;
    font-family: "Noto Serif", serif;
    font-size: 58px;
    color: var(--foam-white);
    transform: rotate(-15deg);
    letter-spacing: 2px;
  }
</style>
</head>
<body>
  <main class="canvas">
    <div class="label-band"></div>
    <section class="badge">
      <svg viewBox="0 0 900 900" width="900" height="900">
        <defs>
          <clipPath id="badge-clip">
            <path d="M450 20 C760 20 880 140 880 450 C880 760 760 880 450 880 C140 880 20 760 20 450 C20 140 140 20 450 20 Z"/>
          </clipPath>
          <linearGradient id="splash-tone" x1="0" y1="0" x2="1" y2="1">
            <stop offset="0" stop-color="var(--splash-light)"/>
            <stop offset="1" stop-color="var(--splash-deep)"/>
          </linearGradient>
        </defs>
        <path class="badge-shape" fill="var(--ocean-blue)"
          d="M450 20 C760 20 880 140 880 450 C880 760 760 880 450 880 C140 880 20 760 20 450 C20 140 140 20 450 20 Z"/>
        <g clip-path="url(#badge-clip)">
          <rect class="splash-area" role="img" aria-label="Water splash illustration with droplets"
            x="0" y="640" width="380" height="260" fill="url(#splash-tone)"/>
        </g>
      </svg>
      <div class="brand-mark">
        <div class="brand-dot"></div>
        <div class="brand-name">SAFIRA</div>
        <div class="tagline">purity water</div>
      </div>
      <div class="volume">500ml</div>
    </section>
  </main>
</body>
</html>
```